COMPANY NAME: Brightmoor Paths: Task Description: We are a new UK based business with global rea

Target Market

- Personal and professional development – 30-55 age group, corporate leaders, Eastern European and Asian markets
- On-assignment projects – Corporate market – Eastern European and Asian Markets
- Property investment - 35-65 age group, Europe, USA, Australia

What we need

We need logos and brand design for a suite of web platforms (website, twitter and Facebook profile). We would like to have a cohesive and consistent look across all of our online platforms. The design suite must therefore include social media logos, backgrounds and headers. Specifically we are looking for:

a. Facebook header/page design: likely to have a more youthful look

b. Website: Header, background and layout that is responsive to devices, iPhone primarily, then tablet, then PC (we have purchased a website building package from GoDaddy so if you are familiar with one of their themes, it would be great to have a design that fits with a theme you would recommend); Design should be able to accommodate a place to position video in the medium term but an image in the short term.

c. LinkedIn: header/logo; more corporate look

d. Twitter: background/logo

e. Powerpoint template: background and logo - simple and soft background not busy

f. Electronic Newsletter: logo, header and sidebar; simple and soft background not busy

h. Business card: sophisticated and simple

Colors

We have in mind a preference for colors from the purple family, maybe lavender, so as to appeal to all genders and age groups. Though we are happy to go with a recommendation if you think otherwise.

We would like a look that is professional, airy, bright, fresh, futuristic, insightful, friendly.

Ethos of the brand

- experiencing opportunity and being fulfilled in a changing world
- services are facilitated through insights
- support provided through our product, services and tailored approach to coaching/partnerships (which includes private client match-making)
- we are service providers and passionate about quality and modern leadership skills at all stages in life.

The company name is "Brightmoor Paths” - our main message is helping people move to the next level - through investments, personal and professional growth.

Some of our messaging

1. International Leadership in a new world.

2. New technology;

3. Informed;

4. Positively Influential

5. Making a difference;

6. Empowered;

7. Risk free investments;

8. Commercial opportunity;

9. Fulfilled living;

10. Carefree and Fun Living;

11. Progression;

12. Open-minded

13. Energy/dynamic

The Business:
The business is to move people very quickly out of situations that hold them back. the situations could be their own personal situations; their career; their jobs; their teams; their ideas; their finances; their financial opportunities. Remove their fears and give them the strategies to take action. The team are international and have 40 years experience between them in this area.

We do want to come across modern and dynamic, customer outcome focussed, building long-term relationships; international.
Updates

Project Deadline Extended
Reason: We have not found the right designs - we are not just looking for a website design but also images and logos. Most images we can see in the designs are stock images - very standard. We need an image which will be the face of the company, like the shop front window. This main image will be used on social media (top image) and also the home page of the website.

Target Market(s)

30-55 years
Eastern Europe; UK; Asia; Africa; Middle East
Personal, Professional, Corporate, and Financial Growth

Industry/Entity Type

Business Service

Contact Information for Business Card

Simple and stylish
the 3 areas of the business on the reverse -

International look - Offices in UK and San Francisco

Company name
web address www.brightmoorpath.com
email director@brightmoorpath.com
Facebook brightmoor path
LinkedIn Brightmoor Path
Twitter Brightmoor Path
Telephone: +44 (0) 712 348 9561

Logo Text

Something that symbolises unlimited growth - probably not text - could use the word INSIGHT in some way

Number of Pages Required

1 page

Colors
e4daeb
f3f1f8
ffffff

Requirements
Must have
• social media symbols and address
• company name
• Harriet Lomax
• Director
• Telephone +44 (0) 712 348 9561
• Website name www.brightmoorpath.co.uk
• Reverse of Card:
• Discreet, Fast, Brightmoor Consultancy
• Corporate, Professional, Personal & Property Investment
Nice to have
• not too angular; soft lines; not too cluttered (possibly social media on the reverse and just logo, name, number on the front?
Should not have
• too busy

```html
<!DOCTYPE html>
<html lang="en">
<head>
<meta charset="utf-8">
<title>Brightmoor Path</title>
<link href="https://fonts.googleapis.com/css2?family=Roboto:wght@400;500;700&family=Open+Sans:ital,wght@0,400;0,600;1,400&display=swap" rel="stylesheet">
<style>
:root{
  --lavender:#e4daeb;
  --lavender-soft:#f3f1f8;
  --lavender-deep:#c4b3d6;
  --accent:#b8a6cc;
  --ink:#222226;
  --body:#6a6a6f;
  --line:#e6e2ea;
  --footer:#2b2b2d;
  --footer-text:#e8e8e8;
  --white:#ffffff;
}
*{margin:0;padding:0;box-sizing:border-box}
html,body{width:1200px;height:2190px;overflow:hidden;background:var(--white)}
body{position:relative;font-family:"Open Sans",Arial,sans-serif;color:var(--body)}
.abs{position:absolute}
h1,h2,h3,h4,.brand{font-family:"Roboto",Arial,sans-serif;color:var(--ink)}

/* hero */
.hero{left:0;top:0;width:1200px;height:520px;background:linear-gradient(180deg,#a08a83 0%,#6f7486 22%,#4d5563 50%,#3d3f47 100%)}
.hero-arrow{top:245px;width:22px;height:32px}
.hero-title{left:507px;top:178px;font-size:55px;font-weight:700;color:var(--white);letter-spacing:1px}
.hero-sub{left:508px;top:240px;font-size:21px;color:var(--white)}
.hero-btn{left:511px;top:285px;width:192px;height:43px;border:2px solid var(--white);color:var(--white);font-family:"Roboto",sans-serif;font-weight:500;font-size:15px;display:flex;align-items:center;justify-content:center;letter-spacing:.5px}

/* side navigation */
.sidenav{left:98px;top:0;width:283px;height:520px}
.sidenav-brand{left:130px;top:45px;font-size:21px;font-weight:500;color:var(--ink)}
.sidenav-list{left:98px;top:150px;width:283px;list-style:none}
.sidenav-list li{height:50px;padding-left:42px;display:flex;align-items:center;border-bottom:1px solid var(--line);font-family:"Roboto",sans-serif;font-size:14px;font-weight:500;color:var(--ink)}
.sidenav-list li:last-child{border-bottom:none}

/* welcome */
.welcome-title{left:0;width:1200px;top:568px;text-align:center;font-size:23px;font-weight:500}
.welcome-text{left:200px;width:800px;top:611px;text-align:center;font-size:13px;line-height:25px}
.service{width:316px;height:244px;top:733px;border:2px solid var(--lavender);text-align:center}
.service-icon{top:-47px;left:101px;width:114px;height:114px;border-radius:50%;background:var(--lavender);display:flex;align-items:center;justify-content:center}
.service h3{margin-top:80px;font-size:17px;font-weight:500}
.service p{margin:14px auto 0;width:270px;font-size:12px;line-height:22px}
.read-more{font-family:"Roboto",sans-serif;font-size:12.5px;font-weight:500;color:var(--accent);letter-spacing:.3px}
.service .read-more{display:block;margin-top:12px}

/* features */
.features{left:0;top:1034px;width:1200px;height:400px;background:var(--lavender-soft)}
.features h2{left:99px;top:1078px;font-size:22px;font-weight:500}
.features-text{left:99px;top:1124px;width:500px;font-size:12px;line-height:25px}
.features-text p{margin-bottom:24px}
.video{left:639px;top:1067px;width:460px;height:326px;background:linear-gradient(135deg,#e9e3dc 0%,#d9d6d3 45%,#c9cfd8 100%)}
.video-bar{left:0;top:0;width:460px;height:25px;background:rgba(20,20,22,.82);color:var(--white);font-size:13px;font-weight:600;padding-left:20px;display:flex;align-items:center}
.video-play{left:203px;top:140px;width:56px;height:56px;border-radius:50%;background:#222;display:flex;align-items:center;justify-content:center}

/* why choose */
.section-title{top:1482px;font-size:22px;font-weight:500}
.why-list{left:99px;top:1540px;width:460px;list-style:none}
.why-list li{position:relative;padding-left:30px;font-size:12px;line-height:22px}
.why-list li svg{position:absolute;left:0;top:4px}
.blog-post{left:588px;width:515px;height:140px}
.blog-thumb{left:0;top:0;width:152px;height:118px}
.blog-body{left:174px;top:0;width:341px}
.blog-body h4{font-size:14px;font-weight:700;line-height:22px;text-decoration:underline;text-underline-offset:3px}
.blog-meta{margin-top:6px;font-size:11px;font-style:italic;color:#a6a6ab;display:flex;gap:14px;align-items:center}
.blog-meta span{display:flex;gap:5px;align-items:center}
.blog-body p{margin-top:6px;font-size:12px;line-height:22px}
.divider{height:1px;background:var(--line)}

/* footer */
.footer{left:0;top:1904px;width:1200px;height:286px;background:var(--footer)}
.footer-brand{left:98px;top:1983px;font-size:26px;font-weight:500;color:var(--white)}
.footer-col h4{font-size:15px;font-weight:500;color:var(--white);margin-bottom:16px}
.footer-links{list-style:none;font-size:12px;line-height:20.5px;color:var(--footer-text)}
.footer-sep{top:1935px;width:1px;height:170px;background:#3c3c3f}
.news-text{font-size:12px;line-height:19px;color:var(--footer-text)}
.news-input{margin-top:14px;width:262px;height:32px;background:var(--white);font-size:12px;color:#777;padding-left:14px;display:flex;align-items:center}
.news-btn{margin-top:10px;width:89px;height:28px;background:var(--accent);color:var(--white);font-family:"Roboto",sans-serif;font-weight:700;font-size:11px;display:flex;align-items:center;justify-content:center}
.contact-row{display:flex;gap:16px;font-size:12px;line-height:19px;color:var(--footer-text);margin-bottom:18px}
.contact-row svg{flex:none;margin-top:3px}
.footer-rule{left:98px;top:2125px;width:1005px;height:1px;background:#3c3c3f}
.copyright{left:99px;top:2149px;font-size:12px;color:var(--footer-text)}
.social{left:960px;top:2141px;display:flex;gap:7px}
.social span{width:33px;height:33px;border:2px solid var(--white);border-radius:50%}
</style>
</head>
<body>

<!-- hero -->
<div class="abs hero" role="img" aria-label="Aerial photograph of a city skyline at dusk with a river beyond"></div>
<svg class="abs hero-arrow" style="left:34px" viewBox="0 0 22 32"><path d="M18 3 5 16l13 13" fill="none" stroke="#fff" stroke-opacity=".75" stroke-width="3"/></svg>
<svg class="abs hero-arrow" style="left:1144px" viewBox="0 0 22 32"><path d="M4 3l13 13L4 29" fill="none" stroke="#fff" stroke-opacity=".75" stroke-width="3"/></svg>
<h1 class="abs hero-title">BRIGHTMOOR PATH</h1>
<p class="abs hero-sub">We are a consulting company in the UK.</p>
<div class="abs hero-btn">GET MORE INFO &gt;&gt;</div>

<!-- side navigation -->
<svg class="abs sidenav" viewBox="0 0 283 520">
  <path d="M0 0h283v460L141 520 0 460z" fill="#fff"/>
  <path d="M0 0h283v108c-40-10-80-18-130-6S40 122 0 114z" fill="#e4daeb"/>
  <path d="M0 114c40 8 90 8 153-12s90-12 130 6v10c-40-14-80-20-130-4S40 128 0 122z" fill="#c4b3d6"/>
</svg>
<div class="abs brand sidenav-brand">BRIGHTMOOR PATH</div>
<ul class="abs sidenav-list">
  <li>ABOUT YOU</li><li>ABOUT US</li><li>OUR VALUES</li><li>TESTIMONIALS</li><li>SOCIAL MEDIA</li><li>NEWS ALERT</li>
</ul>

<!-- welcome -->
<h2 class="abs welcome-title">HELLO AND WELCOME TO THE BRIGHTMOOR PATH</h2>
<p class="abs welcome-text">If you seek an experienced and trusted partner to work with you on an assignment or simply want some strategies to move your personal or professional talents to the next level then you are in the right place.</p>

<div class="abs service" style="left:99px">
  <div class="abs service-icon"><svg width="62" height="50" viewBox="0 0 62 50"><path d="M31 4C17 4 6 12 6 22c0 6 4 11 10 14l-3 9 10-6c3 1 5 1 8 1 14 0 25-8 25-18S45 4 31 4z" fill="none" stroke="#fff" stroke-width="4"/><path d="M20 17h22M20 25h16" stroke="#fff" stroke-width="3"/></svg></div>
  <h3>CONSULTANCY</h3>
  <p>If you feel that the pace of change in business is so fast that to be an outstanding leader you should ensure you are brought</p>
  <span class="read-more">READ MORE &gt;&gt;</span>
</div>
<div class="abs service" style="left:442px">
  <div class="abs service-icon"><svg width="44" height="54" viewBox="0 0 44 54"><path d="M2 2h28l12 12v38H2z" fill="#fff"/><path d="M30 2v12h12" fill="#e4daeb"/><path d="M10 24h24M10 31h24M10 38h24" stroke="#e4daeb" stroke-width="3"/></svg></div>
  <h3>ON ASSIGNMENT</h3>
  <p>If you feel that the pace of change in business is so fast that to be an outstanding leader you should ensure you are brought</p>
  <span class="read-more">READ MORE &gt;&gt;</span>
</div>
<div class="abs service" style="left:785px">
  <div class="abs service-icon"><svg width="48" height="52" viewBox="0 0 48 52"><circle cx="24" cy="14" r="12" fill="#fff"/><path d="M2 50c0-14 10-22 22-22s22 8 22 22z" fill="#fff"/></svg></div>
  <h3>PROPERTY: PRIVATE CLIENT</h3>
  <p>If you feel that the pace of change in business is so fast that to be an outstanding leader you should ensure you are brought</p>
  <span class="read-more">READ MORE &gt;&gt;</span>
</div>

<!-- features -->
<section class="abs features"></section>
<div class="features">
  <h2 class="abs">OUR FEATURES</h2>
  <div class="abs features-text">
    <p>If you seek an experienced and trusted partner to work with you on an assignment or simply want some strategies to move your personal or professional talents to the next level then you are in the right place.</p>
    <p>If you feel that the pace of change in business is so fast that to be an outstanding leader you should ensure you are brought up to speed regularly then you are in the right place.</p>
    <p>If you are hearing about the essential new leadership essentials and you are ready to hear how to adopt them into your life or business then you are at the right place.</p>
    <span class="read-more">READ MORE &gt;&gt;</span>
  </div>
</div>
<div class="abs video" role="img" aria-label="Video still of colleagues reviewing printed charts at a table">
  <div class="abs video-bar">Brightmoor Path</div>
  <div class="abs video-play"><svg width="20" height="22" viewBox="0 0 20 22"><path d="M3 1l16 10L3 21z" fill="#fff"/></svg></div>
</div>

<!-- why choose us -->
<h2 class="abs section-title" style="left:99px">WHY CHOOSE US?</h2>
<ul class="abs why-list">
  <li style="margin-bottom:27px"><svg width="16" height="16" viewBox="0 0 16 16"><circle cx="8" cy="8" r="8" fill="#c4b3d6"/><path d="M4 8l3 3 5-6" fill="none" stroke="#fff" stroke-width="2"/></svg>Nemo enim ipsam voluptatem quia voluptas sit aspernatur aut odit aut fug</li>
  <li style="margin-bottom:27px"><svg width="16" height="16" viewBox="0 0 16 16"><circle cx="8" cy="8" r="8" fill="#c4b3d6"/><path d="M4 8l3 3 5-6" fill="none" stroke="#fff" stroke-width="2"/></svg>Et harum quidem rerum facilis est et expedita distinctio libero tempore</li>
  <li style="margin-bottom:27px"><svg width="16" height="16" viewBox="0 0 16 16"><circle cx="8" cy="8" r="8" fill="#c4b3d6"/><path d="M4 8l3 3 5-6" fill="none" stroke="#fff" stroke-width="2"/></svg>At vero eos et accusamus et iusto odio dignissimos ducimus qui blanditiis praesentium voluptatum deleniti atque corrupti q</li>
  <li style="margin-bottom:27px"><svg width="16" height="16" viewBox="0 0 16 16"><circle cx="8" cy="8" r="8" fill="#c4b3d6"/><path d="M4 8l3 3 5-6" fill="none" stroke="#fff" stroke-width="2"/></svg>Nam libero tempore, cum soluta nobis est eligendi optio cumque nihil</li>
  <li><svg width="16" height="16" viewBox="0 0 16 16"><circle cx="8" cy="8" r="8" fill="#c4b3d6"/><path d="M4 8l3 3 5-6" fill="none" stroke="#fff" stroke-width="2"/></svg>Itaque earum rerum hic tenetur a sapiente delectus, ut aut reiciendis volup maiores alias consequatur aut perferendis dolori.</li>
</ul>
<span class="abs read-more" style="left:99px;top:1845px">READ MORE &gt;&gt;</span>

<!-- latest blog -->
<h2 class="abs section-title" style="left:588px">LATEST BLOG</h2>
<article class="abs blog-post" style="top:1536px">
  <div class="abs blog-thumb" role="img" aria-label="Photo of two business colleagues at a desk with a monitor" style="background:linear-gradient(135deg,#c9d2dc,#8f9fb0 60%,#5f6b78)"></div>
  <div class="abs blog-body">
    <h4>AT VERO EOS ET ACCUSAMUS ET IUSTO ODIODIG NISSIMOS DUCIMUS QUI BLAND</h4>
    <div class="blog-meta"><span>&#9638; 15/10/2015</span><span>&#9679; Mara Ellis</span><span>&#9670; 4 Comments</span></div>
    <p>Duis aute irure dolor in reprehenderit in voluptate velit esse cillum dolore eu fugiat nulla pariatur.</p>
  </div>
</article>
<div class="abs divider" style="left:588px;top:1673px;width:515px"></div>
<article class="abs blog-post" style="top:1694px">
  <div class="abs blog-thumb" role="img" aria-label="Photo of hands reviewing documents and a tablet on a wooden desk" style="background:linear-gradient(135deg,#e6dcd0,#b89a7d 55%,#5d4a3c)"></div>
  <div class="abs blog-body">
    <h4>AT VERO EOS ET ACCUSAMUS ET IUSTO ODIODIG NISSIMOS DUCIMUS QUI BLAND</h4>
    <div class="blog-meta"><span>&#9638; 15/10/2015</span><span>&#9679; Mara Ellis</span><span>&#9670; 4 Comments</span></div>
    <p>Duis aute irure dolor in reprehenderit in voluptate velit esse cillum dolore eu fugiat nulla pariatur.</p>
  </div>
</article>
<div class="abs divider" style="left:588px;top:1829px;width:515px"></div>
<span class="abs read-more" style="left:588px;top:1845px">VIEW MORE &gt;&gt;</span>

<!-- footer -->
<footer class="abs footer"></footer>
<div class="abs brand footer-brand">BRIGHTMOOR PATH</div>
<div class="abs footer-sep" style="left:403px"></div>
<div class="abs footer-sep" style="left:561px"></div>
<div class="abs footer-sep" style="left:884px"></div>
<div class="abs footer-col" style="left:419px;top:1939px">
  <h4>INFORMATION</h4>
  <ul class="footer-links"><li>About You</li><li>About Us</li><li>Our Values</li><li>Testimonials</li><li>Social Media</li><li>News Alert</li></ul>
</div>
<div class="abs footer-col" style="left:595px;top:1939px">
  <h4>NEWSLETTER</h4>
  <p class="news-text">Register Your email address to get<br>information about us</p>
  <div class="news-input">Email Address</div>
  <div class="news-btn">SUBSCRIBE</div>
</div>
<div class="abs footer-col" style="left:911px;top:1939px">
  <h4>CONTACT US</h4>
  <div class="contact-row"><svg width="10" height="14" viewBox="0 0 10 14"><path d="M5 0a5 5 0 0 0-5 5c0 4 5 9 5 9s5-5 5-9a5 5 0 0 0-5-5zm0 7a2 2 0 1 1 0-4 2 2 0 0 1 0 4z" fill="#fff"/></svg><span>27 Larkfield Row, Suite 4,<br>NR2 1QE Norwich</span></div>
  <div class="contact-row"><svg width="12" height="12" viewBox="0 0 12 12"><path d="M2 0l3 3-1.5 2a7 7 0 0 0 3.5 3.5L9 7l3 3-2 2C5 12 0 7 0 2z" fill="#fff"/></svg><span>+44 (0) 712 348 9561</span></div>
  <div class="contact-row"><svg width="13" height="10" viewBox="0 0 13 10"><path d="M0 0h13v10H0z" fill="#fff"/><path d="M0 0l6.5 5L13 0" fill="none" stroke="#2b2b2d" stroke-width="1.2"/></svg><span>Director@brightmoorpath.com</span></div>
</div>
<div class="abs footer-rule"></div>
<p class="abs copyright">Copyrights &copy;2016, Brightmoor Path. All rights reserved.</p>
<div class="abs social" aria-label="Social media links"><span></span><span></span><span></span><span></span></div>

</body>
</html>
```